Business Card Design for Portrait photography professional

We are a small company specializing in portrait photography (weddings, family, couples, children, newborn, pregnant, etc.) Occasionally we do business portraits too and do some other type of photography. We need a business card which would fit into the same look and feel as our website theme (lumvika.com - under construction currently).
Our target customer base lies within mid- to upmarket. We want our business cards to convey a feeling of quality, solidness and a bit luxury.
Design should be universal and usable on 85mmx55mm, 90mmx50mm and 90mmx55mm
one extra file (PSD of a website didn't fit into the allowed updoad, therefore has put it into my filecrate: https://www.filecrate-example.net/s/qt7wk2rbvx9dmhe/website%20theme%20PSD.psd)

Target Market(s)

mostly private people, 25-60 years old, mostly well established.

Industry/Entity Type

Portrait Photography

Requirements
Must have
• 2 sided design (print on both sides of the business card).
Must include:
business name, logo, URL (lumvika.no) , employee name, email address, and phone number.
Colorscheme of the website lumvika.no / lumvika.com

```html
<!DOCTYPE html>
<html lang="en">
<head>
<meta charset="utf-8">
<title>Lumvika Studio – Business Card</title>
<link rel="stylesheet" href="https://fonts.googleapis.com/css2?family=Cinzel:wght@400&family=Pinyon+Script&display=swap">
<style>
  :root {
    --page: #ffffff;
    --card: #0b0a0a;
    --card-edge: #000000;
    --ink: #f4f2ef;
    --panel: rgba(70, 68, 66, 0.55);
    --panel-edge: rgba(255, 255, 255, 0.18);
    --photo-dark: #1a1213;
    --photo-mid: #3a2226;
    --photo-warm: #b88a7f;
  }
  * { margin: 0; padding: 0; box-sizing: border-box; }
  html, body {
    width: 1200px;
    height: 856px;
    overflow: hidden;
    background: var(--page);
  }
  .canvas {
    position: relative;
    width: 1200px;
    height: 856px;
  }
  .card {
    position: absolute;
    left: 124px;
    top: 148px;
    width: 952px;
    height: 537px;
    background: radial-gradient(ellipse at 35% 30%, #1d1b1b 0%, var(--card) 60%);
    border: 3px solid var(--card-edge);
    overflow: hidden;
  }
  .portrait-photo {
    position: absolute;
    right: 20px;
    top: 18px;
    width: 380px;
    height: 500px;
    background:
      radial-gradient(ellipse at 50% 70%, var(--photo-warm) 0%, var(--photo-mid) 38%, transparent 70%),
      linear-gradient(180deg, #0e0b0b 0%, var(--photo-dark) 45%, var(--photo-mid) 100%);
    -webkit-mask-image: linear-gradient(90deg, transparent 0%, #000 40%);
            mask-image: linear-gradient(90deg, transparent 0%, #000 40%);
  }
  .frame {
    position: absolute;
    inset: 0;
    width: 100%;
    height: 100%;
    pointer-events: none;
  }
  .brand-mark {
    position: absolute;
    left: 47px;
    top: 47px;
    width: 190px;
    height: 190px;
    border: 3px solid var(--ink);
    border-radius: 50%;
    display: flex;
    flex-direction: column;
    align-items: center;
    justify-content: center;
  }
  .brand-name, .brand-url {
    font-family: "Cinzel", serif;
    font-weight: 400;
    color: var(--ink);
    text-align: center;
    letter-spacing: 1px;
  }
  .brand-name { font-size: 25px; line-height: 1.2; }
  .brand-url { font-size: 15px; margin-top: 10px; }
  .contact-panel {
    position: absolute;
    left: 29px;
    top: 307px;
    width: 562px;
    height: 210px;
    background: linear-gradient(180deg, rgba(95, 93, 90, 0.6) 0%, var(--panel) 40%, rgba(40, 39, 38, 0.7) 100%);
    border: 1px solid var(--panel-edge);
    border-radius: 8px;
    box-shadow: 0 2px 6px rgba(0, 0, 0, 0.6);
  }
  .person-name {
    position: absolute;
    left: 0;
    width: 100%;
    top: 14px;
    text-align: center;
    font-family: "Pinyon Script", cursive;
    font-size: 56px;
    color: var(--ink);
  }
  .contact-line {
    position: absolute;
    font-family: "Cinzel", serif;
    font-size: 29px;
    line-height: 1;
    color: var(--ink);
  }
  .street { left: 22px; top: 102px; }
  .city { left: 22px; top: 140px; }
  .web { left: 162px; top: 162px; }
  .phone { right: 48px; top: 102px; }
  .fax { right: 48px; top: 140px; }
</style>
</head>
<body>
<main class="canvas">
  <section class="card">
    <div class="portrait-photo" role="img" aria-label="Portrait photograph of a child in a black top hat, hand raised to chin"></div>

    <svg class="frame" viewBox="0 0 946 531" aria-hidden="true">
      <rect x="10" y="10" width="926" height="511" fill="none" stroke="#f4f2ef" stroke-width="3"/>
      <rect x="17" y="17" width="912" height="497" fill="none" stroke="#f4f2ef" stroke-width="1.5"/>
    </svg>

    <div class="brand-mark">
      <span class="brand-name">Lumvika<br>Studio</span>
      <span class="brand-url">lumvika.com</span>
    </div>

    <div class="contact-panel">
      <p class="person-name">Name</p>
      <p class="contact-line street">Street</p>
      <p class="contact-line city">City</p>
      <p class="contact-line web">Web Address</p>
      <p class="contact-line phone">Phone</p>
      <p class="contact-line fax">Fax</p>
    </div>
  </section>
</main>
</body>
</html>
```